KelvrasMassage website required

We need a website for a mobile sports massage therapist in the United Kingdom. Specialising in pregnancy and postnatal massage, sports and remedial, deep tissue massage & Corprate Massage. Attached are some logos that we already have in various colours. The file named logo_white_background is what we normally use. Feel free to use the others at your discretion.

Requirements
Must have
• Service areas, Booking system.

```html
<!DOCTYPE html>
<html lang="en">
<head>
<meta charset="utf-8">
<title>Kelvras Massage</title>
<link href="https://fonts.googleapis.com/css2?family=Lato:ital,wght@0,400;0,700;0,900;1,400;1,700&family=Roboto+Condensed:wght@700&family=Open+Sans:wght@400;600&display=swap" rel="stylesheet">
<style>
:root{
  --sky:#5ec8f5;
  --navy:#0f4a70;
  --green:#8cc63f;
  --green-dark:#7ab32e;
  --ink:#2b2b2b;
  --text:#555;
  --grey-band:#e8e8e8;
  --footer:#333333;
  --white:#fff;
}
*{box-sizing:border-box;margin:0;padding:0}
html,body{width:1200px;height:2469px;overflow:hidden}
body{position:relative;background:var(--white);font-family:"Lato",sans-serif;color:var(--text)}
.abs{position:absolute}
.heading{font-family:"Roboto Condensed",sans-serif;font-weight:700;color:var(--ink);text-transform:uppercase}

/* header */
.site-header{left:0;top:0;width:1200px;height:82px;background:var(--sky)}
.brand{left:173px;top:0;width:123px;height:110px;background:var(--white);display:flex;flex-direction:column;align-items:center;justify-content:center;z-index:3;box-shadow:0 2px 6px rgba(0,0,0,.15)}
.brand span{font-family:"Lato",sans-serif;font-weight:700;font-size:17px;color:var(--sky);line-height:1.15;text-align:center}
.main-nav{left:459px;top:23px;width:423px;height:40px;background:var(--navy);display:flex;align-items:center;justify-content:space-around;padding:0 10px}
.main-nav a{color:var(--white);font-family:"Open Sans",sans-serif;font-size:12px;font-weight:600;text-decoration:none;text-transform:uppercase}
.phone-badge{left:894px;top:23px;width:131px;height:40px;background:var(--green);display:flex;align-items:center;justify-content:center;gap:8px;color:var(--white);font-family:"Open Sans",sans-serif;font-size:12px;font-weight:600;white-space:nowrap}

/* hero */
.hero{left:0;top:82px;width:1200px;height:420px;background:linear-gradient(90deg,#0c0c0c 0%,#3b4a32 25%,#8a9a72 55%,#b6c79a 75%,#7f9a5e 100%)}
.hero-photo{left:872px;top:82px;width:214px;height:420px;background:linear-gradient(180deg,#d8c8b8 0%,#ece8e4 40%,#d9d6d2 100%);opacity:.8}
.hero-tag{left:173px;top:181px;width:160px;height:40px;background:var(--green);color:var(--white);font-weight:700;font-size:18px;display:flex;align-items:center;justify-content:center;border-radius:3px}
.hero-title{left:175px;top:246px;font-size:42px;color:var(--white);white-space:nowrap}
.hero-text{left:178px;top:308px;width:700px;font-size:13px;line-height:22px;color:var(--white)}

/* about */
.accent{background:var(--sky);width:49px;height:49px}
.about-photo{left:209px;top:563px;width:389px;height:346px;background:linear-gradient(160deg,#e4eef2 0%,#b8cdd6 50%,#9fb5bf 100%);border-radius:3px}
.about-title{left:640px;top:565px;font-size:33px;white-space:nowrap}
.about-sub{left:640px;top:620px;font-style:italic;color:var(--green);font-size:15px}
.about-text{left:640px;top:656px;width:385px;font-size:12.5px;line-height:24.5px;text-align:justify}
.btn-video{left:640px;top:844px;width:135px;height:36px;background:var(--green);color:var(--white);font-size:15px;display:flex;align-items:center;justify-content:center;gap:8px;border-radius:3px}

/* section heads */
.section-title{left:0;width:1200px;text-align:center;font-size:30px}
.rule{left:584px;width:32px;height:2px;background:var(--ink)}
.section-sub{left:400px;width:400px;text-align:center;font-size:11.5px;line-height:20px;color:#333}

/* service cards */
.card-frame{width:270px;height:362px;border:1.5px solid var(--green)}
.card-frame.featured{background:var(--green)}
.card{width:238px;height:331px;background:var(--white);box-shadow:0 2px 8px rgba(0,0,0,.25);text-align:center}
.card-photo{position:absolute;left:26px;top:22px;width:186px;height:122px}
.card h3{position:absolute;left:0;top:174px;width:100%;font-size:12.5px;font-weight:700;color:var(--ink)}
.card p{position:absolute;left:22px;top:206px;width:194px;font-size:12.5px;line-height:20px;color:#444}
.card .more{position:absolute;left:74px;top:287px;width:90px;height:28px;border:1px solid var(--green);border-radius:14px;font-size:9px;color:var(--green);display:flex;align-items:center;justify-content:center}
.featured .more{background:var(--green);color:var(--white)}

/* team */
.member{width:197px;height:258px;text-align:center}
.member-photo{position:absolute;left:0;top:0;width:197px;height:194px}
.member-name{position:absolute;left:0;top:212px;width:100%;font-size:14px;color:var(--ink)}
.member-role{position:absolute;left:0;top:234px;width:100%;font-size:8.5px;color:#888}
.member-line{position:absolute;left:8px;top:257px;width:181px;height:1px;background:#ddd}
.member.active .member-name,.member.active .member-role{color:var(--white)}
.member-panel{position:absolute;left:0;top:194px;width:197px;height:66px;background:#34353d}
.member-social{position:absolute;left:0;top:169px;width:197px;height:25px;background:var(--green);display:flex;justify-content:center;align-items:center;gap:16px}
.member-social i{width:8px;height:8px;border-radius:50%;background:var(--white);display:block}

/* band */
.band{left:0;top:1985px;width:1200px;height:324px;background:var(--grey-band)}
.band-title{font-size:20px}
.band-title em{font-style:normal;color:var(--green)}
.commit-text{left:157px;top:2076px;width:420px;font-size:13px;line-height:21px;color:#333}
.ticks{left:157px;top:2150px;list-style:none}
.ticks li{display:flex;align-items:center;gap:10px;height:31px;font-size:13px;color:#333}
.band-divider{left:594px;top:2040px;width:1px;height:240px;background:#ccc}
.slider-btn{width:24px;height:24px;background:var(--white);border:1px solid #ccc;display:flex;align-items:center;justify-content:center}
.quote{left:625px;top:2077px;width:407px;height:120px;background:var(--white);border-radius:6px;padding:14px 18px 0 40px;font-style:italic;font-size:11.5px;line-height:18px;color:#333}
.quote-mark{left:640px;top:2086px;font-size:34px;color:#bbb;font-family:Georgia,serif;line-height:1}
.avatar{left:645px;top:2225px;width:59px;height:59px;border-radius:50%;background:linear-gradient(180deg,#777,#333);border:3px solid var(--white)}
.client-name{left:724px;top:2248px;font-size:11px;font-weight:700;color:var(--green)}

/* footer */
.footer-nav{left:0;top:2309px;width:1200px;height:61px;background:var(--green)}
.footer-links{left:157px;top:2330px;display:flex;gap:18px;color:var(--white);font-size:14px;font-family:"Open Sans",sans-serif}
.follow{left:856px;top:2326px;display:flex;align-items:center;gap:10px;color:var(--white);font-size:20px;font-weight:700}
.follow i{width:27px;height:27px;border-radius:50%;background:var(--white);display:block}
.footer-base{left:0;top:2370px;width:1200px;height:99px;background:var(--footer)}
.contact{display:flex;align-items:center;gap:12px;color:var(--white)}
.contact .dot{width:27px;height:27px;border-radius:50%;background:var(--green);display:flex;align-items:center;justify-content:center}
.contact b{display:block;font-size:14px;font-weight:700}
.contact small{display:block;font-size:9px;color:#ccc}
.footer-brand{left:800px;top:2390px;width:240px;text-align:center;color:var(--white)}
.footer-brand strong{display:block;font-family:"Roboto Condensed",sans-serif;font-size:21px;letter-spacing:.5px}
.footer-brand span{display:block;font-size:11px;line-height:17px}
</style>
</head>
<body>

<header class="abs site-header"></header>
<div class="abs brand"><span>Kelvras<br>Massage</span></div>
<nav class="abs main-nav">
  <a>Home</a><a>About Us</a><a>Services ▾</a><a>Inquiry</a><a>Contact Us</a>
</nav>
<div class="abs phone-badge">
  <svg width="18" height="16" viewBox="0 0 18 16"><path d="M2 5c0-2 2-3 7-3s7 1 7 3v2h-3V5H5v2H2z M4 8h10l2 6H2z" fill="#fff"/></svg>
  012 345 6789
</div>

<section class="abs hero"></section>
<div class="abs hero-photo" role="img" aria-label="Smiling pregnant woman in a white top outdoors"></div>
<div class="abs hero-tag">Specialising in</div>
<h1 class="abs heading hero-title">Pregnancy and Postnatal Massage</h1>
<p class="abs hero-text">Sed ut perspiciatis unde omnis iste natus error sit voluptatem accusantium doloremque laudantium, totam rem aperiam, eaque ipsa quae ab illo inventore veritatis et quasi veritatis et quasi architecto beatae vitae dicta sunt explicabo. Sed ut perspiciatis unde omnis iste natus error..</p>

<div class="abs accent" style="left:194px;top:546px"></div>
<div class="abs accent" style="left:565px;top:874px"></div>
<div class="abs about-photo" role="img" aria-label="Clinic corridor with staff in white coats"></div>
<h2 class="abs heading about-title">KelvrasMassage</h2>
<p class="abs about-sub">Sed ut perspiciatis unde omnis</p>
<p class="abs about-text">Sed ut perspiciatis unde omnis iste natus error sit voluptatem accusantium doloremque laudantium, totam rem aperiam, eaque ipsa quae ab illo inventore veritatis et quasi veritatis et quasi architecto beatae vitae dicta sunt explicabo. Sed ut perspiciatis unde omnis iste natus error.<br>Sed ut perspiciatis unde omnis iste natus error sit voluptatem accusantium doloremque laudantium.</p>
<div class="abs btn-video">Watch Video
  <svg width="14" height="14" viewBox="0 0 14 14"><circle cx="7" cy="7" r="6" fill="none" stroke="#fff"/><path d="M5.5 4.5v5l4-2.5z" fill="#fff"/></svg>
</div>

<h2 class="abs heading section-title" style="top:984px">Services</h2>
<div class="abs rule" style="top:1031px"></div>
<p class="abs section-sub" style="top:1042px">Sed ut perspiciatis unde omnis iste natus error sitvoluptatem accusantium doloremque laudantium.</p>

<div class="abs card-frame" style="left:173px;top:1123px"></div>
<div class="abs card" style="left:188px;top:1137px">
  <div class="card-photo" role="img" aria-label="Woman stretching during a pregnancy exercise class" style="background:linear-gradient(135deg,#e8e4e6,#d77fb0 55%,#eee)"></div>
  <h3>Pregnancy and Postnatal Massage</h3>
  <p>Lorem ipsum dolor sit amet, con-sectetuer adipiscing elit, dolore magna aliquam erat volutpat..</p>
  <div class="more">View Details</div>
</div>
<div class="abs card-frame featured" style="left:466px;top:1123px"></div>
<div class="abs card featured" style="left:481px;top:1137px">
  <div class="card-photo" role="img" aria-label="Two runners on a seaside promenade" style="background:linear-gradient(180deg,#b9d3e6,#8aa0b0 55%,#5e5e66)"></div>
  <h3>Sports and Remedial</h3>
  <p>Lorem ipsum dolor sit amet, con-sectetuer adipiscing elit, dolore magna aliquam erat volutpat..</p>
  <div class="more">View Details</div>
</div>
<div class="abs card-frame" style="left:757px;top:1123px"></div>
<div class="abs card" style="left:772px;top:1137px">
  <div class="card-photo" role="img" aria-label="Therapist massaging a client's leg" style="background:linear-gradient(135deg,#f2ece6,#d9a98a 55%,#b07d5e)"></div>
  <h3>Deep Tissue &amp; Corprate Massage</h3>
  <p>Lorem ipsum dolor sit amet, con-sectetuer adipiscing elit, dolore magna aliquam erat volutpat..</p>
  <div class="more">View Details</div>
</div>

<h2 class="abs heading section-title" style="top:1534px">Our Speciality</h2>
<div class="abs rule" style="top:1581px"></div>
<p class="abs section-sub" style="top:1592px">Sed ut perspiciatis unde omnis iste natus error sitvoluptatem accusantium doloremque laudantium.</p>

<div class="abs member" style="left:173px;top:1671px">
  <div class="member-photo" role="img" aria-label="Portrait of a therapist in a blue shirt" style="background:linear-gradient(180deg,#e6e6e6,#7fa9d6)"></div>
  <div class="member-name">Member Name</div><div class="member-role">Pregnancy and Postnatal Massage</div><div class="member-line"></div>
</div>
<div class="abs member active" style="left:392px;top:1671px">
  <div class="member-photo" role="img" aria-label="Portrait of a therapist in a suit" style="background:linear-gradient(180deg,#eef0f0,#8a8f96)"></div>
  <div class="member-social"><i></i><i></i><i></i><i></i></div>
  <div class="member-panel"></div>
  <div class="member-name">Member Name</div><div class="member-role">Sports and Remedial</div>
</div>
<div class="abs member" style="left:611px;top:1671px">
  <div class="member-photo" role="img" aria-label="Portrait of a therapist in a blue shirt" style="background:linear-gradient(180deg,#f4f4f4,#3f6ea0)"></div>
  <div class="member-name">Member Name</div><div class="member-role">Deep Tissue &amp; Corprate Massage</div><div class="member-line"></div>
</div>
<div class="abs member" style="left:830px;top:1671px">
  <div class="member-photo" role="img" aria-label="Portrait of a therapist in a checked shirt" style="background:linear-gradient(180deg,#dfe6ea,#7f9ec4)"></div>
  <div class="member-name">Member Name</div><div class="member-role">Sports and Remedial</div><div class="member-line"></div>
</div>

<section class="abs band"></section>
<h2 class="abs heading band-title" style="left:153px;top:2024px">Our <em>Commitment to Customers</em></h2>
<p class="abs commit-text">Loren autem vel eum iriure hendrerit in vulputate velit esse molestie. onsectetuer adipiscing elit, sed diam nonummy nibh euismod tincidunt u eu feugiat nulla facilisis.</p>
<ul class="abs ticks">
  <li><svg width="13" height="13" viewBox="0 0 13 13"><circle cx="6.5" cy="6.5" r="6.5" fill="#8cc63f"/><path d="M3.5 6.7l2 2 4-4" stroke="#fff" stroke-width="1.6" fill="none"/></svg>Autem vel eum iriure hendrerit in</li>
  <li><svg width="13" height="13" viewBox="0 0 13 13"><circle cx="6.5" cy="6.5" r="6.5" fill="#8cc63f"/><path d="M3.5 6.7l2 2 4-4" stroke="#fff" stroke-width="1.6" fill="none"/></svg>Gendrerit in vulputate velit</li>
  <li><svg width="13" height="13" viewBox="0 0 13 13"><circle cx="6.5" cy="6.5" r="6.5" fill="#8cc63f"/><path d="M3.5 6.7l2 2 4-4" stroke="#fff" stroke-width="1.6" fill="none"/></svg>Autem vel eum adipiscing elit, sed diam</li>
  <li><svg width="13" height="13" viewBox="0 0 13 13"><circle cx="6.5" cy="6.5" r="6.5" fill="#8cc63f"/><path d="M3.5 6.7l2 2 4-4" stroke="#fff" stroke-width="1.6" fill="none"/></svg>Eeum iriure hendrerit in vulputate velit</li>
</ul>
<div class="abs band-divider"></div>
<h2 class="abs heading band-title" style="left:625px;top:2024px">Client <em>Testimonials</em></h2>
<div class="abs slider-btn" style="left:979px;top:2024px"><svg width="8" height="10"><path d="M6 1L2 5l4 4" stroke="#666" fill="none" stroke-width="1.5"/></svg></div>
<div class="abs slider-btn" style="left:1007px;top:2024px"><svg width="8" height="10"><path d="M2 1l4 4-4 4" stroke="#666" fill="none" stroke-width="1.5"/></svg></div>
<div class="abs quote">Lorem ipsum dolor sit amet consetug e sed diay nibh euismodl tincidunt ut laoreet dolore magam er vol wisi enim ad minim veniam quis nostrud exerci tationorem ipsum dolor sit ametee sed diammmy nibh euismd tincidunt ut laoreet dolore magna aliqur volpatl tiidunt ut laoreet dolore magna aliqur volpatl r sit ametee.</div>
<svg class="abs" style="left:920px;top:2196px" width="40" height="22"><path d="M0 0h40L10 22z" fill="#fff"/></svg>
<div class="abs quote-mark">“</div>
<div class="abs avatar" role="img" aria-label="Client portrait"></div>
<div class="abs client-name">Mr. Owen Callister</div>

<nav class="abs footer-nav"></nav>
<div class="abs footer-links"><span>HOME</span><span>|</span><span>ABOUT US</span><span>|</span><span>SERVICES</span><span>|</span><span>INQUIRY</span><span>|</span><span>CONTACT US</span></div>
<div class="abs follow">Follow Us: <i></i><i></i></div>

<footer class="abs footer-base"></footer>
<div class="abs contact" style="left:157px;top:2398px">
  <span class="dot"><svg width="10" height="14" viewBox="0 0 10 14"><path d="M5 0a5 5 0 0 1 5 5c0 4-5 9-5 9S0 9 0 5a5 5 0 0 1 5-5z" fill="#fff"/><circle cx="5" cy="5" r="2" fill="#8cc63f"/></svg></span>
  <div><b>KelvrasMassage</b><small>Your Company Address</small></div>
</div>
<div class="abs contact" style="left:405px;top:2398px">
  <span class="dot"><svg width="12" height="12" viewBox="0 0 12 12"><path d="M2 0l2.5 3-1.5 1.5a7 7 0 0 0 4.5 4.5L9 7.5l3 2.5-1.5 2C5 12 0 7 0 1.5z" fill="#fff"/></svg></span>
  <div><b>Call Us :</b><small>012.345.6789</small></div>
</div>
<div class="abs contact" style="left:585px;top:2398px">
  <span class="dot"><svg width="12" height="9" viewBox="0 0 12 9"><rect width="12" height="9" fill="#fff"/><path d="M0 0l6 5 6-5" stroke="#8cc63f" fill="none"/></svg></span>
  <div><b>Email Us :</b><small>hello@kelvras.example</small></div>
</div>
<div class="abs footer-brand"><strong>KELVRASMASSAGE</strong><span>© 2018 Kelvras Massage.</span><span>All Rights Reserved.</span></div>

</body>
</html>
```